Business Design for Printed Shipping Tape

We need a company logo design to be printed on packaging natural color WAT tape for shipping boxes. www.brightmeadowkelp.com
The tape is 3" wide. Repeat pattern every 10 inches.
Would like our website vertical at one end side and "The Future of Nutrition" on the opposite end.

Industry/Entity Type

Health, Nutrition

Font styles to use
Sans Serif

Requirements
Must have
• Company Logo (attached) website and text "The Future of Nutrition"
Nice to have
• Tape is Natural Color.

```html
<!DOCTYPE html>
<html lang="en">
<head>
<meta charset="utf-8">
<title>Bright Meadow Kelp – Shipping Tape</title>
<link rel="stylesheet" href="https://fonts.googleapis.com/css2?family=Jost:wght@400;600;700&display=swap">
<style>
  :root {
    --kelp-green: #008a6e;
    --ink: #231f20;
    --paper: #ffffff;
    --backdrop: #ffffff;
  }
  * { margin: 0; padding: 0; box-sizing: border-box; }
  html, body {
    width: 1100px;
    height: 1200px;
    overflow: hidden;
    background: var(--backdrop);
  }
  .tape-strip {
    position: absolute;
    left: 79px;
    top: 456px;
    width: 906px;
    height: 287px;
    background: var(--paper);
    box-shadow: 0 14px 40px rgba(0, 0, 0, 0.10);
    overflow: hidden;
    font-family: "Jost", sans-serif;
  }
  .tape-art {
    position: absolute;
    inset: 0;
  }
  .brand-block {
    position: absolute;
    left: 30px;
    top: 40px;
    width: 340px;
    text-align: center;
  }
  .brand-mark {
    width: 38px;
    height: 38px;
    margin: 0 auto 10px;
    border-radius: 50%;
    background: var(--kelp-green);
  }
  .brand-name {
    font-weight: 700;
    font-size: 46px;
    line-height: 0.98;
    letter-spacing: -1px;
    color: var(--ink);
    text-transform: uppercase;
  }
  .brand-tagline {
    display: inline-block;
    margin-top: 10px;
    padding: 0 14px;
    border: 1.5px solid var(--ink);
    font-weight: 400;
    font-size: 13px;
    line-height: 16px;
    letter-spacing: 2px;
    color: var(--ink);
    text-transform: uppercase;
  }
  .slogan {
    position: absolute;
    left: 413px;
    width: 400px;
    top: 98px;
    text-align: center;
    color: var(--paper);
    font-weight: 600;
  }
  .slogan-lead {
    display: block;
    font-size: 42px;
    line-height: 40px;
  }
  .slogan-main {
    display: block;
    font-size: 78px;
    line-height: 66px;
  }
  .website {
    position: absolute;
    left: 861px;
    top: 145px;
    transform: translate(-50%, -50%) rotate(-90deg);
    white-space: nowrap;
    font-weight: 600;
    font-size: 13px;
    letter-spacing: 1px;
    color: var(--ink);
    text-transform: uppercase;
  }
</style>
</head>
<body>
  <section class="tape-strip" aria-label="Shipping tape repeat panel">
    <svg class="tape-art" width="906" height="287" viewBox="0 0 906 287" aria-hidden="true">
      <g class="dot-row" fill="none" stroke="var(--kelp-green)" stroke-width="1.2">
        <circle cx="33" cy="258" r="2.6"/>
        <circle cx="42" cy="258" r="2.6"/>
        <circle cx="51" cy="258" r="2.6"/>
        <circle cx="60" cy="258" r="2.6"/>
      </g>
      <g class="dot-column" fill="none" stroke="var(--kelp-green)" stroke-width="1.2">
        <circle cx="400" cy="64" r="2.6"/>
        <circle cx="400" cy="73" r="2.6"/>
        <circle cx="400" cy="82" r="2.6"/>
        <circle cx="400" cy="91" r="2.6"/>
      </g>

      <path class="slogan-panel" fill="var(--kelp-green)" d="M420 0 H805 C795 30 815 60 805 95 C795 130 815 165 805 200 C795 235 815 260 806 287 H412 C420 250 405 220 413 180 C420 140 405 110 413 70 C420 40 405 20 420 0 Z"/>
    </svg>

    <div class="brand-block">
      <div class="brand-mark"></div>
      <h1 class="brand-name">Bright<br>Meadow<br>Kelp</h1>
      <p class="brand-tagline">A Taste of the Tide</p>
    </div>

    <h2 class="slogan">
      <span class="slogan-lead">The Future of</span>
      <span class="slogan-main">Nutrition</span>
    </h2>

    <p class="website">www.brightmeadowkelp.com</p>
  </section>
</body>
</html>
```